Cover for nonfiction/memoir book "Static Beneath My Skin"

We're looking for a *nonfiction* *memoir* look that is consistent with other covers in that genre.

MUST HAVE:
- It must include the BACK COVER as it will be for print as well as an ebook.
- Title: Static Beneath My Skin
- TITLE MUST BE EASILY READ AT BRINDLECART THUMBNAIL SIZE
- Author name: Dorothea Quell
- At least one of the attached photos of Dorothea
- In COLOR
- The synopsis below
- Space for an endorsement

From the author: "I am looking for a cover that is eye catching and interesting or artistic, rather than just glamorous or pretty. If you like to edit the photos please do not completely remove the wrinkle between my eyebrows as I mention this in the book. It is okay if i look non conventional and my inner Aspie shows a little. The book is a little bit girly, and it would be good for the cover to reflect that, but mildly. No bright pink and purple designs. Please feel free to zoom in or crop the photos as you think works best"

SYNOPSIS (needs to go on the back cover)

Static Beneath My Skin is an acutely honest and often highly entertaining memoir by Dorothea Quell about life with Asperger's Syndrome. The book follows Dorothea in exploring her past and takes the reader with her on her journey to receiving and accepting her diagnosis. Instead of rehashing widely available Asperger's information, Dorothea focuses on discussing the thoughts, feelings and ideas that go along with being an Aspie, giving us a rare peek into what it really feels like to be a person on the spectrum. A must read for all those who enjoy deep personal stories or have a loved one on the spectrum that they wish to understand better.

The book dimensions will be 5x8 trade paperback and 6x9 hardcover (plus 0.25 bleed margin on all sizes - for both sizes).
Here is some more information from the publisher on cover requirements:

"I've attached a sample of both a paperback and hardcover size. Note that the spine width will be different depending on the final length of the book, so it won't be exact. That said, the front and back covers, and the flaps (for the hardcover) will always be the same as shown.
For deliverables, we need the following:

a Creative Suite 6 or earlier native .PSD (Photoshop), .ID (InDesign), or .AI (Illustrator) file. Creative Cloud files cannot be used and will not be accepted.
final file must include layered objects, and cannot be one 'background' image
Final files must be in CMYK color mode, 300dpi minimum
Total Ink saturation must be no more than 240% on any part of the cover. "True" black should use the following CMYK values: 60/40/40/100.
Fonts used in creation of the cover must be either A) embedded or B) sent with the final file
Vector art is preferred for scaling purposes"

Target Market(s)

Women of all ages. People who like psychology and personal stories.
Also parents and family members who may have a loved one on the Autism spectrum.

Requirements
Nice to have
• Bright green new leaves and greenery are good but not necessary.

```html
<!DOCTYPE html>
<html lang="en">
<head>
<meta charset="utf-8">
<title>Static Beneath My Skin — Full Cover</title>
<link rel="stylesheet" href="https://fonts.googleapis.com/css2?family=Cormorant+Garamond:ital,wght@0,500;1,600;1,700&family=Crimson+Text&display=swap">
<style>
  :root {
    --back-light: #f3efb8;
    --back-mid: #e3e48f;
    --back-edge: #b9cf5e;
    --title-red: #b3121b;
    --title-deep: #8a0c13;
    --body-ink: #2a2618;
    --spine-ink: #2d2a1c;
    --sky-top: #7fb0de;
    --sky-haze: #e8f0f4;
    --field-light: #a9c45a;
    --field-deep: #3f6a1c;
    --dress-dark: #2a2238;
    --dress-warm: #8a3a3a;
    --skin-tone: #d9a98c;
    --author-white: #ffffff;
  }
  html, body {
    margin: 0;
    padding: 0;
    width: 1200px;
    height: 856px;
    overflow: hidden;
    background: #ffffff;
  }
  .cover {
    position: relative;
    width: 1200px;
    height: 856px;
    overflow: hidden;
  }
  .back-panel {
    position: absolute;
    left: 0; top: 0;
    width: 630px; height: 856px;
    background: radial-gradient(ellipse at 45% 40%, var(--back-light) 0%, var(--back-mid) 60%, var(--back-edge) 100%);
  }
  .front-photo {
    position: absolute;
    left: 630px; top: 0;
    width: 570px; height: 856px;
    background: linear-gradient(180deg,
      var(--sky-top) 0%, #b8d3ea 22%, var(--sky-haze) 38%,
      var(--field-light) 43%, #7fa23a 70%, var(--field-deep) 100%);
  }
  .author-portrait {
    position: absolute;
    left: 630px; top: 290px;
    width: 420px; height: 430px;
    border-radius: 48% 52% 30% 20% / 40% 40% 30% 30%;
    background: radial-gradient(ellipse at 70% 25%, var(--skin-tone) 0%, #b58a6a 22%, var(--dress-warm) 45%, var(--dress-dark) 80%);
    opacity: 0.92;
  }
  .title {
    position: absolute;
    margin: 0;
    text-align: center;
    font-family: "Cormorant Garamond", Georgia, serif;
    font-style: italic;
    font-weight: 700;
    line-height: 1;
  }
  .title .main { display: block; color: var(--title-red); }
  .title .sub { display: block; font-weight: 600; color: var(--title-deep); }
  .back-title { left: 0; width: 580px; top: 140px; }
  .back-title .main { font-size: 70px; }
  .back-title .sub { font-size: 42px; margin-top: 2px; }
  .front-title {
    left: 630px; width: 570px; top: 50px;
    text-shadow: 2px 3px 4px rgba(60, 0, 0, 0.45);
  }
  .front-title .main { font-size: 128px; }
  .front-title .sub { font-size: 70px; color: var(--title-red); margin-top: 0; }
  .synopsis {
    position: absolute;
    left: 64px; top: 268px;
    width: 438px;
    margin: 0;
    font-family: "Crimson Text", Georgia, serif;
    font-size: 17.4px;
    line-height: 27.6px;
    text-align: justify;
    color: var(--body-ink);
  }
  .endorsement-space {
    position: absolute;
    left: 64px; top: 620px;
    width: 438px; height: 170px;
  }
  .spine-text {
    position: absolute;
    writing-mode: vertical-rl;
    font-family: "Cormorant Garamond", Georgia, serif;
    color: var(--spine-ink);
    white-space: nowrap;
  }
  .spine-title { left: 578px; top: 204px; font-style: italic; font-weight: 600; font-size: 36px; }
  .spine-author { left: 584px; top: 640px; font-weight: 500; font-size: 28px; }
  .front-author {
    position: absolute;
    left: 630px; width: 570px; top: 786px;
    margin: 0;
    text-align: center;
    font-family: "Cormorant Garamond", Georgia, serif;
    font-weight: 500;
    font-size: 46px;
    line-height: 1;
    color: var(--author-white);
    text-shadow: 1px 2px 3px rgba(0, 0, 0, 0.5);
  }
</style>
</head>
<body>
<div class="cover">
  <section class="back-panel" role="img" aria-label="Soft pale green background framed by sprigs of fresh young leaves"></section>

  <h2 class="title back-title">
    <span class="main">Static</span>
    <span class="sub">beneath my skin</span>
  </h2>
  <p class="synopsis">Static Beneath My Skin is an acutely honest and often highly entertaining memoir by Dorothea Quell about life with Asperger's Syndrome. The book follows Dorothea in exploring her past and takes the reader with her on her journey to receiving and accepting her diagnosis. Instead of rehashing widely available Asperger's information, Dorothea focuses on discussing the thoughts, feelings and ideas that go along with being an Aspie, giving us a rare peek into what it really feels like to be a person on the spectrum. A must read for all those who enjoy deep personal stories or have a loved one on the spectrum that they wish to understand better.</p>
  <div class="endorsement-space" aria-hidden="true"></div>

  <div class="spine-text spine-title">Static Beneath My Skin</div>
  <div class="spine-text spine-author">Dorothea Quell</div>

  <section class="front-photo" role="img" aria-label="Green meadow under a pale blue sky with soft clouds"></section>
  <div class="author-portrait" role="img" aria-label="Photograph of Dorothea in a dark floral dress lying in the grass, glancing sideways, holding a notebook and pen"></div>

  <h1 class="title front-title">
    <span class="main">Static</span>
    <span class="sub">beneath my skin</span>
  </h1>
  <p class="front-author">Dorothea Quell</p>
</div>
</body>
</html>
```